Hollowmere Dental Center Specials/Offers

Take the advertisement pic (LABELED ADVERTISEMENT) and make it look "professional in appearance" using the logo and color scheme of Hollowmere Dental Center. The Phone number should be 719-555-0186. I want the same content, different background, professional looking document. I want it to be a 12"x12" document. High resolution files should include .PDF, .JPG and .AI. Any or all documents can be used for colors and overall scheme. I would like to have the overall colors include the main blue color from the file 4db749b4ef4c5e0717512bf7eb26bf54 and include the brown "swoosh" somewhere through/on the final document. Stock files of smiling young families can be used but not required. I am on a tight time-line and have placed 5 days as the deadline, but I will pick my favorite in as little as 2-3 days if I can get a good product. Again ALL the info from the Advertisement document should be included on the final product. Use any or all of the uploaded files for assistance. You can also visit our website for more info: www.hollowmeredentalcenter.example Thanks

```html
<!DOCTYPE html>
<html lang="en">
<head>
<meta charset="utf-8">
<title>Hollowmere Dental Center – Family Ad</title>
<link rel="stylesheet" href="https://fonts.googleapis.com/css2?family=Questrial&family=Mulish:wght@800&family=PT+Sans:wght@400;700&display=swap">
<style>
  :root {
    --teal: #688f9c;
    --teal-top: #7898a3;
    --sky: #dfe8ec;
    --white: #ffffff;
    --brown: #5a4a42;
    --ink: #3d3532;
    --backdrop: #eeeeee;
    --photo-a: #c9b2a3;
    --photo-b: #8d7466;
  }
  * { margin: 0; padding: 0; box-sizing: border-box; }
  html, body { width: 1019px; height: 1200px; overflow: hidden; background: var(--backdrop); }
  .ad {
    position: absolute; left: 0; top: 90px;
    width: 1019px; height: 1019px; overflow: hidden;
    background: linear-gradient(180deg, var(--teal-top) 0%, var(--sky) 26%, var(--white) 42%, var(--white) 100%);
    font-family: "PT Sans", sans-serif;
  }
  .headline {
    position: absolute; top: 72px; left: 0; width: 100%;
    text-align: center; color: var(--white);
    font-family: "Questrial", sans-serif; font-size: 42px; letter-spacing: 0.5px;
  }
  .headline strong { font-family: "Mulish", sans-serif; font-weight: 800; }
  .brand { position: absolute; left: 64px; top: 232px; color: var(--brown); }
  .brand-name {
    display: flex; align-items: center; gap: 14px;
    font-family: "Questrial", sans-serif; font-size: 36px; line-height: 1;
  }
  .brand-dot { width: 18px; height: 18px; border-radius: 50%; background: var(--teal); }
  .brand-tagline {
    margin-top: 12px; margin-left: 32px;
    font-family: "Questrial", sans-serif; font-size: 16px; letter-spacing: 1.5px;
  }
  .photo {
    position: absolute; left: 400px; top: 250px; width: 600px; height: 560px;
    border-radius: 260px 260px 0 0;
    background: radial-gradient(ellipse at 55% 40%, var(--photo-a) 0%, var(--photo-b) 80%, var(--photo-b) 100%);
  }
  .wave { position: absolute; left: 0; top: 0; width: 1019px; height: 1019px; }
  .dentist {
    position: absolute; left: 57px; top: 782px;
    font-size: 23px; font-weight: 700; color: var(--brown); letter-spacing: 0.3px;
  }
  .dentist .title { font-size: 19px; border-left: 2px solid var(--brown); padding-left: 9px; margin-left: 6px; }
  .address { position: absolute; left: 53px; top: 822px; font-size: 21px; line-height: 29px; color: var(--ink); }
  .contact {
    position: absolute; left: 570px; top: 856px; list-style: none;
    font-size: 23px; line-height: 33px; color: var(--white);
  }
  .contact li { display: flex; align-items: center; gap: 8px; }
  .contact svg { width: 22px; height: 22px; fill: var(--white); flex: none; }
</style>
</head>
<body>
  <main class="ad">
    <h1 class="headline">Where the <strong>Whole Family</strong> can be Seen!</h1>

    <div class="brand">
      <div class="brand-name"><span class="brand-dot"></span>Hollowmere Dental Center</div>
      <div class="brand-tagline">FAMILY • COSMETIC • IMPLANTS</div>
    </div>

    <div class="photo" role="img" aria-label="Smiling couple showing healthy white teeth"></div>

    <svg class="wave" viewBox="0 0 768 768" preserveAspectRatio="none" aria-hidden="true">
      <path d="M0 672 C 120 712, 250 712, 360 680 C 500 640, 620 520, 768 472 L 768 768 L 0 768 Z" fill="var(--white)"/>
      <path d="M0 672 C 60 700, 150 706, 230 690 C 360 660, 450 600, 560 540 C 640 500, 710 480, 768 472 L 768 768 L 0 768 Z" fill="var(--teal)"/>
    </svg>

    <p class="dentist">DANIEL R. HOLLOWMERE<span class="title">D.D.S.</span></p>
    <p class="address">4820 Larkspur Dr. Suite B<br>Colorado Springs, CO 80918</p>

    <ul class="contact">
      <li><svg viewBox="0 0 24 24"><path d="M6.6 10.8a15 15 0 0 0 6.6 6.6l2.2-2.2a1 1 0 0 1 1-.25 11 11 0 0 0 3.6.57 1 1 0 0 1 1 1V20a1 1 0 0 1-1 1A17 17 0 0 1 3 4a1 1 0 0 1 1-1h3.5a1 1 0 0 1 1 1c0 1.25.2 2.45.57 3.57a1 1 0 0 1-.25 1z"/></svg>(719) 555-0186</li>
      <li><svg viewBox="0 0 24 24"><path d="M6 2h12v5H6zM3 8h18a1 1 0 0 1 1 1v8h-4v5H6v-5H2V9a1 1 0 0 1 1-1zm5 7v5h8v-5z"/></svg>(719) 555-0147</li>
      <li><svg viewBox="0 0 24 24"><path d="M2 5h20v14H2zm2 2v.4l8 5.2 8-5.2V7z"/></svg>hello@hollowmeredentalcenter.example</li>
      <li><svg viewBox="0 0 24 24"><path d="M12 2a10 10 0 1 0 0 20 10 10 0 0 0 0-20zm0 2a8 8 0 0 1 7.7 6H16V8h-3V5h-1zM4 12a8 8 0 0 1 .3-2L9 14.6V16h2v3.9A8 8 0 0 1 4 12zm9 7.9V17h3l2.5 1A8 8 0 0 1 13 19.9z"/></svg>www.hollowmeredentalcenter.example</li>
    </ul>
  </main>
</body>
</html>
```